Casas de Nueva Aurora Flyer

Make me a flyer postcard 5 x 7 horizontal, one sided. I want main title to be "Casas de Nueva Aurora". It needs to say “Familias que se forman en la fe y valores humanos, y trabajan para llevar a otras familias al encuentro con Cristo y la Virgen María.”  We are in 4 places, include this:
Reuniones Cada Domingo
Los Olmos, Falls Church: 11:15am - 301-555-0142
Monte Claro, Sterling: 9:30am - 571-555-0187
Hogar Valle Sereno, 9:45am - 703-555-0163
Puerta Dorada, Winchester: 2:30pm - 540-555-0129
Include the logo attached, and use the picture attached as the main image, you can select the people from the image only and delete background or keep background but make it fit in nicely to the postcard.

```html
<!DOCTYPE html>
<html lang="es">
<head>
<meta charset="utf-8">
<title>Casas de Nueva Aurora – Postal</title>
<link rel="stylesheet" href="https://fonts.googleapis.com/css2?family=Outfit:wght@100;300;400&family=Fira+Sans:ital,wght@1,800;1,900&family=Lexend:wght@300;700&display=swap">
<style>
  :root {
    --page: #d9dadc;
    --brown-dark: #3a2115;
    --brown-mid: #5a3a25;
    --tan: #c9a47a;
    --tan-deep: #a9814f;
    --cream: #f6efdf;
    --cream-light: #fffaf0;
    --gold: #d6b17d;
    --text-dark: #2a170e;
    --white: #ffffff;
  }
  html, body {
    margin: 0;
    width: 1200px;
    height: 1200px;
    overflow: hidden;
    background: var(--page);
  }
  .flyer {
    position: absolute;
    left: 40px;
    top: 200px;
    width: 1120px;
    height: 800px;
    overflow: hidden;
    background: var(--tan);
    box-shadow: 0 12px 30px rgba(0,0,0,0.25);
  }
  .flyer-shapes {
    position: absolute;
    inset: 0;
  }
  .title-light {
    position: absolute;
    left: 52px;
    top: 20px;
    margin: 0;
    font-family: "Outfit", sans-serif;
    font-weight: 100;
    font-size: 138px;
    line-height: 1;
    letter-spacing: -3px;
    color: var(--text-dark);
    white-space: nowrap;
  }
  .title-bold {
    position: absolute;
    right: 318px;
    top: 138px;
    margin: 0;
    font-family: "Fira Sans", sans-serif;
    font-style: italic;
    font-weight: 900;
    font-size: 92px;
    line-height: 1;
    letter-spacing: -2px;
    color: var(--text-dark);
    text-shadow: 3px 3px 0 var(--tan-deep);
    white-space: nowrap;
  }
  .mission {
    position: absolute;
    left: 41px;
    top: 254px;
    width: 780px;
    margin: 0;
    font-family: "Outfit", sans-serif;
    font-weight: 300;
    font-size: 25px;
    line-height: 31px;
    color: var(--white);
  }
  .schedule-heading {
    position: absolute;
    left: 780px;
    top: 475px;
    width: 340px;
    height: 34px;
    margin: 0;
    background: linear-gradient(90deg, rgba(214,177,125,0) 0%, var(--gold) 35%, #e8cfa5 100%);
    font-family: "Fira Sans", sans-serif;
    font-style: italic;
    font-weight: 800;
    font-size: 22px;
    line-height: 36px;
    color: var(--white);
    padding-left: 18px;
    box-sizing: border-box;
    text-shadow: 1px 1px 2px rgba(58,33,21,0.6);
  }
  .meetings {
    position: absolute;
    left: 775px;
    top: 532px;
    margin: 0;
    padding: 0;
    list-style: none;
  }
  .meeting {
    display: flex;
    width: 304px;
    height: 41px;
    margin-bottom: 21px;
    border: 2px solid var(--tan);
    border-radius: 7px;
    overflow: hidden;
    box-sizing: border-box;
    font-family: "Lexend", sans-serif;
  }
  .meeting-place {
    width: 150px;
    background: var(--tan);
    color: var(--white);
    font-weight: 300;
    font-size: 13px;
    line-height: 15px;
    padding: 4px 0 0 20px;
    box-sizing: border-box;
    position: relative;
  }
  .meeting-place svg {
    position: absolute;
    left: 6px;
    top: 5px;
  }
  .meeting-info {
    flex: 1;
    background: var(--brown-dark);
    color: var(--white);
    padding: 2px 0 0 28px;
    position: relative;
  }
  .meeting-time {
    display: block;
    font-weight: 700;
    font-size: 17px;
    line-height: 19px;
  }
  .meeting-phone {
    display: block;
    font-weight: 300;
    font-size: 12.5px;
    line-height: 15px;
  }
  .meeting-info .icon-clock { position: absolute; left: 8px; top: 5px; }
  .meeting-info .icon-phone { position: absolute; left: 8px; top: 22px; }
</style>
</head>
<body>
<main class="flyer">
  <svg class="flyer-shapes" viewBox="0 0 1120 800" width="1120" height="800">
    <defs>
      <linearGradient id="baseGlow" x1="0" y1="0" x2="1" y2="0">
        <stop offset="0" stop-color="#b08a5c"/>
        <stop offset="0.45" stop-color="#ece0c8"/>
        <stop offset="0.8" stop-color="#f4ecdc"/>
        <stop offset="1" stop-color="#c29d6c"/>
      </linearGradient>
      <linearGradient id="creamBand" x1="0" y1="0" x2="1" y2="0">
        <stop offset="0" stop-color="#f6efdf" stop-opacity="0"/>
        <stop offset="0.4" stop-color="#f8f1e2" stop-opacity="0.7"/>
        <stop offset="0.85" stop-color="#fffaf0"/>
        <stop offset="1" stop-color="#fbf4e6"/>
      </linearGradient>
      <linearGradient id="photoTone" x1="0" y1="0" x2="0" y2="1">
        <stop offset="0" stop-color="#efe5cf"/>
        <stop offset="0.35" stop-color="#9a9066"/>
        <stop offset="0.7" stop-color="#6c5a4a"/>
        <stop offset="1" stop-color="#c7a57a"/>
      </linearGradient>
      <linearGradient id="darkPanel" x1="0" y1="0" x2="1" y2="1">
        <stop offset="0" stop-color="#4a2c1c"/>
        <stop offset="0.5" stop-color="#3a2115"/>
        <stop offset="1" stop-color="#2f1a10"/>
      </linearGradient>
      <linearGradient id="iconTone" x1="0" y1="0" x2="0" y2="1">
        <stop offset="0" stop-color="#b8332a"/>
        <stop offset="0.6" stop-color="#c9452b"/>
        <stop offset="1" stop-color="#d9892f"/>
      </linearGradient>
    </defs>

    <rect class="base" width="1120" height="800" fill="url(#baseGlow)"/>

    <!-- group photo area -->
    <polygon role="img" aria-label="Foto de grupo de las familias reunidas al aire libre"
             points="0,362 840,362 474,800 0,800" fill="url(#photoTone)" opacity="0.9"/>

    <!-- right brown panel with gold edge -->
    <polygon points="1120,42 1120,800 466,800" fill="var(--gold)"/>
    <polygon points="1120,49 1120,800 474,800" fill="url(#darkPanel)"/>

    <!-- title light band -->
    <rect x="0" y="147" width="845" height="93" fill="url(#creamBand)"/>

    <!-- mission band -->
    <rect x="0" y="240" width="845" height="4" fill="var(--cream)"/>
    <rect x="0" y="244" width="845" height="114" fill="var(--brown-dark)"/>
    <rect x="0" y="358" width="845" height="4" fill="var(--gold)"/>

    <!-- framed icon -->
    <polygon points="841,88 961,41 1081,88 1081,379 841,379" fill="#7b6a44"/>
    <polygon points="851,93 961,52 1071,93 1071,369 851,369" fill="#a8935c"/>
    <polygon role="img" aria-label="Icono de la Sagrada Familia en marco dorado"
             points="862,100 961,64 1060,100 1060,358 862,358" fill="url(#iconTone)"/>
  </svg>

  <h1 class="title">
    <span class="title-light">Casas de</span>
    <span class="title-bold">Nueva Aurora</span>
  </h1>

  <p class="mission">Familias que se forman en la fe y valores humanos, y trabajan para llevar a otras familias al encuentro con Cristo y la Virgen María.</p>

  <h2 class="schedule-heading">Reuniones Cada Domingo</h2>

  <ul class="meetings">
    <li class="meeting">
      <div class="meeting-place">
        <svg width="9" height="12" viewBox="0 0 9 12"><path d="M4.5 0A4.5 4.5 0 0 0 0 4.5C0 8 4.5 12 4.5 12S9 8 9 4.5A4.5 4.5 0 0 0 4.5 0Zm0 6.3a1.8 1.8 0 1 1 0-3.6 1.8 1.8 0 0 1 0 3.6Z" fill="#3a2115"/></svg>
        Los Olmos,<br>Falls Church
      </div>
      <div class="meeting-info">
        <svg class="icon-clock" width="11" height="11" viewBox="0 0 12 12"><circle cx="6" cy="6" r="6" fill="#c9a47a"/><path d="M6 2.5V6l2.3 1.5" stroke="#3a2115" stroke-width="1.4" fill="none"/></svg>
        <svg class="icon-phone" width="11" height="11" viewBox="0 0 12 12"><path d="M2.4 0.5 4.3 2.6 3.3 4.2c.8 1.8 2.3 3.3 4.3 4.4l1.5-1.1 2.2 1.9-1 2c-4.8-.1-9.6-4.8-9.7-9.7Z" fill="#c9a47a"/></svg>
        <span class="meeting-time">11:15am</span>
        <span class="meeting-phone">301-555-0142</span>
      </div>
    </li>
    <li class="meeting">
      <div class="meeting-place">
        <svg width="9" height="12" viewBox="0 0 9 12"><path d="M4.5 0A4.5 4.5 0 0 0 0 4.5C0 8 4.5 12 4.5 12S9 8 9 4.5A4.5 4.5 0 0 0 4.5 0Zm0 6.3a1.8 1.8 0 1 1 0-3.6 1.8 1.8 0 0 1 0 3.6Z" fill="#3a2115"/></svg>
        Monte Claro,<br>Sterling
      </div>
      <div class="meeting-info">
        <svg class="icon-clock" width="11" height="11" viewBox="0 0 12 12"><circle cx="6" cy="6" r="6" fill="#c9a47a"/><path d="M6 2.5V6l2.3 1.5" stroke="#3a2115" stroke-width="1.4" fill="none"/></svg>
        <svg class="icon-phone" width="11" height="11" viewBox="0 0 12 12"><path d="M2.4 0.5 4.3 2.6 3.3 4.2c.8 1.8 2.3 3.3 4.3 4.4l1.5-1.1 2.2 1.9-1 2c-4.8-.1-9.6-4.8-9.7-9.7Z" fill="#c9a47a"/></svg>
        <span class="meeting-time">9:30am</span>
        <span class="meeting-phone">571-555-0187</span>
      </div>
    </li>
    <li class="meeting">
      <div class="meeting-place">
        <svg width="9" height="12" viewBox="0 0 9 12"><path d="M4.5 0A4.5 4.5 0 0 0 0 4.5C0 8 4.5 12 4.5 12S9 8 9 4.5A4.5 4.5 0 0 0 4.5 0Zm0 6.3a1.8 1.8 0 1 1 0-3.6 1.8 1.8 0 0 1 0 3.6Z" fill="#3a2115"/></svg>
        Hogar<br>Valle Sereno
      </div>
      <div class="meeting-info">
        <svg class="icon-clock" width="11" height="11" viewBox="0 0 12 12"><circle cx="6" cy="6" r="6" fill="#c9a47a"/><path d="M6 2.5V6l2.3 1.5" stroke="#3a2115" stroke-width="1.4" fill="none"/></svg>
        <svg class="icon-phone" width="11" height="11" viewBox="0 0 12 12"><path d="M2.4 0.5 4.3 2.6 3.3 4.2c.8 1.8 2.3 3.3 4.3 4.4l1.5-1.1 2.2 1.9-1 2c-4.8-.1-9.6-4.8-9.7-9.7Z" fill="#c9a47a"/></svg>
        <span class="meeting-time">9:45am</span>
        <span class="meeting-phone">703-555-0163</span>
      </div>
    </li>
    <li class="meeting">
      <div class="meeting-place">
        <svg width="9" height="12" viewBox="0 0 9 12"><path d="M4.5 0A4.5 4.5 0 0 0 0 4.5C0 8 4.5 12 4.5 12S9 8 9 4.5A4.5 4.5 0 0 0 4.5 0Zm0 6.3a1.8 1.8 0 1 1 0-3.6 1.8 1.8 0 0 1 0 3.6Z" fill="#3a2115"/></svg>
        Puerta Dorada,<br>Winchester
      </div>
      <div class="meeting-info">
        <svg class="icon-clock" width="11" height="11" viewBox="0 0 12 12"><circle cx="6" cy="6" r="6" fill="#c9a47a"/><path d="M6 2.5V6l2.3 1.5" stroke="#3a2115" stroke-width="1.4" fill="none"/></svg>
        <svg class="icon-phone" width="11" height="11" viewBox="0 0 12 12"><path d="M2.4 0.5 4.3 2.6 3.3 4.2c.8 1.8 2.3 3.3 4.3 4.4l1.5-1.1 2.2 1.9-1 2c-4.8-.1-9.6-4.8-9.7-9.7Z" fill="#c9a47a"/></svg>
        <span class="meeting-time">2:30pm</span>
        <span class="meeting-phone">540-555-0129</span>
      </div>
    </li>
  </ul>
</main>
</body>
</html>
```